High end business card design for custom homebuilding company

Looking for a high end business card design that is unique and elegant. Can use embossing, foil printing, laser die cutting, or any high end printing technique or high end paper. Will upload current design so you can see the logo and what we are using currently, but we want something more unique and elegant. I included our logo to help with design.

Target Market(s)

High end custom home buyers of $1.5 million plus homes. Also real estate developers of high end communities.

Industry/Entity Type

Business

Contact Information for Business Card

Double sided. We want something very elegant and expensive looking. We are looking to incorporate a combination of perhaps linen paper or a high end paper, with foil stamping or embossing/debossing to make the card look unique, but still elegant. We tend to use blacks and golds, but are open to any ideas. Looking for creative and unique design.

Colors

Designer to choose colors to be used in the design.

Requirements
Must have
• High end, elegant look. Can use foil, embossing, or high end papers like linen. We want to make the card unique and interesting, but elegant and expensive looking.
Nice to have
• I am including just some cards I saw that looked interesting for one reason or another. I like a clean elegant design and like both the clean white style, and the blacks. So not sure if we want a black design or white. Would like to see both.

```html
<!DOCTYPE html>
<html lang="en">
<head>
<meta charset="utf-8">
<title>Ridgeline Custom Homes – Business Card</title>
<link href="https://fonts.googleapis.com/css2?family=Open+Sans:wght@400;600&display=swap" rel="stylesheet">
<style>
  :root {
    --page-bg: #e6e7e9;
    --card-edge: #1c1c1e;
    --metal-dark: #2a2b2d;
    --metal-mid: #3b3c3f;
    --mesh-tone: #8e9196;
    --mesh-light: #b4b7bb;
    --gold: #c9b23a;
    --white: #f4f4f4;
  }
  * { margin: 0; padding: 0; box-sizing: border-box; }
  html, body {
    width: 1200px; height: 970px; overflow: hidden;
    background: var(--page-bg);
    font-family: "Open Sans", Arial, sans-serif;
  }
  .card {
    position: absolute; left: 100px; top: 210px;
    width: 1000px; height: 551px;
    border-radius: 30px;
    background: linear-gradient(180deg, var(--metal-mid) 0%, var(--metal-dark) 50%, var(--metal-mid) 100%);
    border: 6px solid var(--card-edge);
    overflow: hidden;
  }
  .mesh-band {
    position: absolute; left: 10px; right: 10px;
    background: linear-gradient(180deg, var(--mesh-light), var(--mesh-tone));
    opacity: .85;
  }
  .mesh-band.top { top: 8px; height: 74px; border-radius: 22px 22px 0 0; }
  .mesh-band.bottom { bottom: 8px; height: 68px; border-radius: 0 0 22px 22px; }
  .wordmark {
    position: absolute; left: 48px; top: 102px;
    color: var(--white); font-weight: 600;
    font-size: 44px; letter-spacing: 2px; line-height: 1;
    text-transform: uppercase;
  }
  .wordmark-sub { display: block; font-size: 18px; letter-spacing: 14px; margin-top: 8px; color: var(--gold); }
  .contact { position: absolute; left: 48px; top: 196px; color: var(--white); }
  .contact-name { color: var(--gold); font-weight: 600; font-size: 25px; line-height: 32px; letter-spacing: .5px; text-transform: uppercase; }
  .contact-title { font-size: 20px; line-height: 28px; }
  .contact-address { font-size: 20px; line-height: 30px; margin-top: 12px; }
  .contact-list { list-style: none; margin-top: 8px; }
  .contact-list li { display: flex; align-items: center; gap: 12px; font-size: 20px; line-height: 31px; }
  .contact-list svg { width: 18px; height: 18px; flex: none; }
  .brand-mark {
    position: absolute; left: 470px; top: 80px; width: 500px; height: 380px;
    display: flex; align-items: center; justify-content: center;
    color: var(--white); font-weight: 600; font-size: 60px; letter-spacing: 6px;
    text-transform: uppercase;
  }
</style>
</head>
<body>
  <div class="card">
    <div class="mesh-band top" role="img" aria-label="Perforated metal mesh band"></div>
    <div class="mesh-band bottom" role="img" aria-label="Perforated metal mesh band"></div>

    <div class="wordmark">Ridgeline<span class="wordmark-sub">Custom Homes</span></div>

    <div class="contact">
      <div class="contact-name">Daniel Hart</div>
      <div class="contact-title">Managing Director</div>
      <div class="contact-address">2740 Harbor Crest Lane,<br>Palm Cove FL 32190</div>
      <ul class="contact-list">
        <li>
          <svg viewBox="0 0 24 24" fill="var(--gold)"><path d="M6.6 10.8a15.1 15.1 0 0 0 6.6 6.6l2.2-2.2a1 1 0 0 1 1-.25 11.4 11.4 0 0 0 3.6.57 1 1 0 0 1 1 1V20a1 1 0 0 1-1 1A17 17 0 0 1 3 4a1 1 0 0 1 1-1h3.5a1 1 0 0 1 1 1c0 1.25.2 2.45.57 3.57a1 1 0 0 1-.25 1z"/></svg>
          + 555 010 0199
        </li>
        <li>
          <svg viewBox="0 0 24 24" fill="var(--gold)"><path d="M2 5h20v14H2z"/><path d="M2 5l10 8 10-8" fill="none" stroke="var(--metal-dark)" stroke-width="1.6"/></svg>
          info@ridgelinehomes.com
        </li>
        <li>
          <svg viewBox="0 0 24 24" fill="none" stroke="var(--gold)" stroke-width="1.8"><circle cx="12" cy="12" r="9"/><ellipse cx="12" cy="12" rx="4" ry="9"/><path d="M3 12h18M5 7h14M5 17h14"/></svg>
          info@ridgelinehomes.com
        </li>
      </ul>
    </div>

    <div class="brand-mark">Ridgeline</div>
  </div>
</body>
</html>
```